KRM BUSINESS CARD

I'd like a new business card for the folks in my office. I recently became aware of a company that produces extra thick cards that seem to me to make excellent use of embossing. I have a logo that I like so I just need a design that uses embossing effectively, is simple and uses minimal color.

I am uploading our current logo of a tooth with a brush above it. I am also uploading another file with the words of our business. In your design please use the square version of the tooth vs. the strectched version. The original logo is the more square image but please use the words and the fonts of "Fennimore Dental Group" and incorporate that in the design.

Industry/Entity Type

Business

Colors
ffffff

Requirements
Must have
• Logo, company name (also a part of our existing logo), employee name and title, phone number and website address. Must be simple
Nice to have
• Embossed - Maybe a solid color on the back
Should not have
• Must not be too complex or busy

```html
<!DOCTYPE html>
<html lang="en">
<head>
<meta charset="utf-8">
<title>Fennimore Dental Group – Business Card</title>
<link rel="stylesheet" href="https://fonts.googleapis.com/css2?family=Tinos:wght@400&display=swap">
<style>
  :root {
    --bg: #ece6dc;
    --card-black: #050505;
    --card-white: #f7f7f7;
    --brand-blue: #33409a;
    --brand-green: #1fa34a;
    --ink: #1a1a1a;
    --rule: #8a8a8a;
    --white: #ffffff;
  }
  * { box-sizing: border-box; margin: 0; padding: 0; }
  html, body { width: 1200px; height: 1023px; overflow: hidden; background: var(--bg); }
  .canvas { position: relative; width: 1200px; height: 1023px; }

  .card {
    position: absolute;
    left: 220px;
    width: 760px;
    height: 434px;
    border-radius: 18px;
    overflow: hidden;
    box-shadow: 0 6px 18px rgba(0,0,0,.18);
  }

  /* Back */
  .card-back { top: 50px; background: var(--card-black); }
  .back-brand {
    position: absolute; left: 70px; top: 150px; right: 40px;
    display: flex; align-items: center; gap: 30px;
  }
  .back-brand .mark-square {
    width: 150px; height: 150px; flex: none;
    background: var(--brand-blue);
  }
  .back-brand .brand-name {
    font-family: "Tinos", serif; font-weight: 400;
    font-size: 44px; line-height: 1.1;
    color: var(--white);
    white-space: nowrap;
  }
  .back-url {
    position: absolute; right: 40px; bottom: 34px;
    font-family: "Tinos", serif; font-size: 22px; color: var(--white);
  }

  /* Front */
  .card-front { top: 539px; background: var(--card-white); }
  .front-rule {
    position: absolute; left: 0; right: 0; top: 150px;
    height: 1px; background: var(--rule);
  }
  .front-mark {
    position: absolute; left: 270px; top: 48px;
    display: flex; align-items: center; gap: 14px;
    background: var(--card-white); padding: 0 14px;
  }
  .front-mark .mark-square { width: 90px; height: 90px; background: var(--brand-blue); }
  .front-mark .mark-name {
    font-family: "Tinos", serif; font-size: 44px; color: var(--brand-blue);
  }
  .staff {
    position: absolute; left: 300px; top: 182px;
    font-family: "Tinos", serif;
  }
  .staff .staff-name { font-size: 30px; color: var(--brand-blue); text-transform: uppercase; letter-spacing: .5px; }
  .staff .staff-title { font-size: 20px; color: var(--ink); margin-left: 60px; }
  .contact {
    position: absolute; left: 48px; top: 268px;
    list-style: none; font-family: "Tinos", serif; font-size: 20px; color: var(--ink);
  }
  .contact li { display: flex; align-items: center; gap: 12px; height: 32px; }
  .contact svg { width: 18px; height: 18px; flex: none; }
  .stripe-blue { position: absolute; left: 0; right: 0; bottom: 30px; height: 8px; background: var(--brand-blue); }
  .stripe-green { position: absolute; left: 0; right: 0; bottom: 0; height: 22px; background: var(--brand-green); }
</style>
</head>
<body>
<main class="canvas">

  <section class="card card-back" aria-label="Card back">
    <div class="back-brand">
      <span class="mark-square"></span>
      <h1 class="brand-name">Fennimore Dental Group</h1>
    </div>
    <p class="back-url">www.fennimoredentalgroup.com</p>
  </section>

  <section class="card card-front" aria-label="Card front">
    <div class="front-rule"></div>
    <div class="front-mark">
      <span class="mark-square"></span>
      <span class="mark-name">KRM</span>
    </div>
    <div class="staff">
      <p class="staff-name">Dana Whitlow</p>
      <p class="staff-title">office manager</p>
    </div>
    <ul class="contact">
      <li>
        <svg viewBox="0 0 24 24" aria-hidden="true"><path fill="var(--brand-green)" d="M6.6 10.8a15 15 0 0 0 6.6 6.6l2.2-2.2a1 1 0 0 1 1-.25 11.4 11.4 0 0 0 3.6.57 1 1 0 0 1 1 1V20a1 1 0 0 1-1 1A17 17 0 0 1 3 4a1 1 0 0 1 1-1h3.5a1 1 0 0 1 1 1c0 1.25.2 2.45.57 3.57a1 1 0 0 1-.25 1z"/></svg>
        555-014-7320
      </li>
      <li>
        <svg viewBox="0 0 24 24" aria-hidden="true"><rect x="2" y="5" width="20" height="14" fill="none" stroke="var(--brand-green)" stroke-width="2"/><path d="M2 5l10 8 10-8" fill="none" stroke="var(--brand-green)" stroke-width="2"/></svg>
        danawhitlow@email.com
      </li>
      <li>
        <svg viewBox="0 0 24 24" aria-hidden="true"><circle cx="12" cy="12" r="10" fill="var(--brand-green)"/><path d="M2 12h20M12 2c3 3 3 17 0 20M12 2c-3 3-3 17 0 20" fill="none" stroke="var(--white)" stroke-width="1.5"/></svg>
        www.fennimoredentalgroup.com
      </li>
    </ul>
    <div class="stripe-blue"></div>
    <div class="stripe-green"></div>
  </section>

</main>
</body>
</html>
```